Business Card Design

New business card design

Target Market(s)

Residential & Commercial Property Managers

Industry/Entity Type

Plumbing Services

Contact Information for Business Card

Name - Owen Tredgold, title - Director, Phone Number - 0431 862 507, email - owen@rvb-plumbing.com.au, Company ABN - 73 215 904 386,

Font styles to use
Sans Serif

Colors
0054AA
0677BA
7BADD7
CADEEF
E8F1F8

```html
<!DOCTYPE html>
<html lang="en">
<head>
<meta charset="utf-8">
<title>RVB Plumbing – Business Card</title>
<link href="https://fonts.googleapis.com/css2?family=Poppins:wght@300;400;500;600&display=swap" rel="stylesheet">
<style>
  :root {
    --backdrop: #c1c1c1;
    --card: #ffffff;
    --ink: #1f2328;
    --brand-blue: #21a8de;
    --band-light: #2bb7e9;
    --band-deep: #21a8de;
    --on-band: #ffffff;
  }
  * { margin: 0; padding: 0; box-sizing: border-box; }
  html, body {
    width: 1200px; height: 979px; overflow: hidden;
    background: var(--backdrop);
    font-family: "Poppins", sans-serif;
    color: var(--ink);
  }
  .card {
    position: absolute;
    left: 353px;
    width: 532px; height: 304px;
    background: var(--card);
    overflow: hidden;
  }
  .card--front { top: 110px; }
  .card--back { top: 520px; height: 303px; }

  .water-band {
    position: absolute; left: 0; right: 0; bottom: 0;
    background: linear-gradient(180deg, var(--band-light) 0%, var(--band-deep) 40%, var(--band-deep) 100%);
  }
  .card--front .water-band { top: 234px; }
  .card--back .water-band { top: 230px; }

  .brand {
    position: absolute;
    display: flex; align-items: center; gap: 8px;
    color: var(--ink);
    font-weight: 400;
    letter-spacing: 1px;
    line-height: 1;
    white-space: nowrap;
  }
  .brand-dot {
    width: 9px; height: 9px; border-radius: 50%;
    background: var(--brand-blue);
  }
  .card--front .brand {
    left: 0; right: 0; top: 122px; justify-content: center;
    font-size: 38px;
  }
  .card--back .brand {
    left: 437px; top: 118px; transform: translateX(-50%);
    font-size: 25px; gap: 6px;
  }
  .card--back .brand-dot { width: 7px; height: 7px; }

  .front-footer {
    position: absolute; left: 0; right: 0; top: 263px;
    display: flex; justify-content: center; align-items: center; gap: 14px;
    color: var(--on-band);
    font-size: 15px; font-weight: 300; line-height: 22px;
  }
  .front-footer .divider {
    width: 7px; height: 7px; background: var(--on-band);
  }

  .person { position: absolute; left: 19px; top: 70px; }
  .person-name { font-size: 23px; font-weight: 400; line-height: 1.2; }
  .person-name .first { color: var(--brand-blue); font-weight: 600; }
  .person-title { font-size: 17px; font-weight: 400; margin-top: 0; line-height: 1.3; }

  .contacts { position: absolute; left: 19px; top: 143px; list-style: none; }
  .contacts li {
    display: flex; align-items: center; gap: 16px;
    font-size: 17px; font-weight: 300; height: 29px;
  }
  .contact-icon { width: 19px; height: 17px; display: block; }
  .contact-icon rect { fill: var(--brand-blue); }
  .contact-icon path { fill: none; stroke: #fff; stroke-width: 1.3; stroke-linejoin: round; stroke-linecap: round; }
  .contact-icon .solid { fill: #fff; stroke: none; }
</style>
</head>
<body>

<section class="card card--front" aria-label="Card front">
  <div class="brand"><span>rvb plumbing</span><span class="brand-dot"></span></div>
  <div class="water-band" role="img" aria-label="Blue water band along the bottom edge"></div>
  <div class="front-footer">
    <span>rvb-plumbing.com.au</span>
    <span class="divider"></span>
    <span>ABN - 73 215 904 386</span>
  </div>
</section>

<section class="card card--back" aria-label="Card back">
  <div class="person">
    <p class="person-name"><span class="first">Owen</span> Tredgold</p>
    <p class="person-title">Director</p>
  </div>
  <ul class="contacts">
    <li>
      <svg class="contact-icon" viewBox="0 0 19 17" aria-hidden="true">
        <rect width="19" height="17"/>
        <path class="solid" d="M6 3.5 L8 3.5 L8.8 6 L7.5 7.2 C8.2 8.8 9.4 10 11 10.7 L12.2 9.4 L14.7 10.2 L14.7 12.2 C14.7 12.8 14.2 13.3 13.5 13.3 C9 13 5.3 9.3 5 4.7 C5 4 5.4 3.5 6 3.5 Z"/>
      </svg>
      <span>0431 862 507</span>
    </li>
    <li>
      <svg class="contact-icon" viewBox="0 0 19 17" aria-hidden="true">
        <rect width="19" height="17"/>
        <path d="M4 5 H15 V12.5 H4 Z M4 5 L9.5 9.5 L15 5 M4 12.5 L8 8.5 M15 12.5 L11 8.5"/>
      </svg>
      <span>owen@rvb-plumbing.com.au</span>
    </li>
  </ul>
  <div class="brand"><span>rvb plumbing</span><span class="brand-dot"></span></div>
  <div class="water-band" role="img" aria-label="Blue water band along the bottom edge"></div>
</section>

</body>
</html>
```